Quick 1hr job to create exciting page header & footer designs

We need some exciting and engaging header and footer designs for school yearbooks, in particular for the NZ Primary school market (children 5 to 10 years old).
The header and footer designs need to be bright and colourful, and should appeal to younger children. Header and footer graphics do not need to be the same, but should at least relate to each other thematically.
Please include the following sample text on the header: Sports Day.
Please include this sample text on the footer: Primary School Name 2014.
Note that the header/footers may be used without the text so the design should work with or without the text. Header/footer may be used over top of a coloured or graphic background. The graphic could be illustrative, photographic or patterned, the more creative the better.

Header dimensions: 198.88 mm w x 15.24 mm h
Footer dimensions: 198.88 mm w x 6.35 mm h

Please see the example pages provided, but please note we are looking for something more suitable for Primary Schools, and a lot more dynamic and interesting!

Target Market(s)

New Zealand Primary Schools

Industry/Entity Type

School

Requirements
Must have
• Must contain sample text and must be suitable for younger children
• Must be appropriate for the New Zealand market, i.e. don't use imagery that is obviously from other countries.

```html
<!DOCTYPE html>
<html lang="en">
<head>
<meta charset="UTF-8">
<title>Sports Day – Header and Footer Set</title>
<link href="https://fonts.googleapis.com/css2?family=Questrial&display=swap" rel="stylesheet">
<style>
  :root {
    --page-bg: #ffffff;
    --ink: #111111;
    --teal: #12a898;
    --teal-light: #8fe0d6;
    --forest: #257a55;
    --forest-mid: #5fae88;
    --forest-light: #d6eee2;
    --orange: #f7941d;
    --orange-light: #fdd09a;
    --lime: #8cc63f;
    --lime-light: #dcefc0;
  }
  html, body {
    margin: 0;
    padding: 0;
    overflow: hidden;
  }
  body {
    width: 1200px;
    height: 900px;
    background: var(--page-bg);
    position: relative;
    font-family: "Questrial", sans-serif;
    color: var(--ink);
  }
  .band {
    position: absolute;
    left: 166px;
    width: 847px;
    display: flex;
    align-items: center;
  }
  .band-pattern {
    position: absolute;
    inset: 0;
  }
  .band-title {
    position: relative;
    margin: 0;
    font-weight: 400;
    letter-spacing: -0.3px;
    white-space: nowrap;
  }
  .header-band { height: 64px; }
  .header-band .band-title { font-size: 27px; }
  .footer-band { height: 27px; }
  .footer-band .band-title { font-size: 16px; }

  .header-teal { top: 96px; justify-content: center; }
  .header-teal .band-pattern {
    background:
      radial-gradient(ellipse 70px 40px at 8% 30%, var(--teal-light), transparent 70%),
      radial-gradient(ellipse 80px 44px at 27% 75%, var(--teal-light), transparent 70%),
      radial-gradient(ellipse 70px 40px at 48% 25%, var(--teal-light), transparent 70%),
      radial-gradient(ellipse 80px 44px at 70% 70%, var(--teal-light), transparent 70%),
      radial-gradient(ellipse 70px 40px at 92% 35%, var(--teal-light), transparent 70%),
      var(--teal);
  }
  .header-teal .band-title { margin-left: -3px; }

  .footer-forest { top: 214px; }
  .footer-forest svg { position: absolute; inset: 0; }
  .footer-forest .band-title { position: absolute; left: 330px; }

  .header-orange { top: 536px; justify-content: flex-end; }
  .header-orange .band-pattern {
    background:
      radial-gradient(ellipse 70px 40px at 6% 70%, var(--orange-light), transparent 70%),
      radial-gradient(ellipse 80px 44px at 25% 28%, var(--orange-light), transparent 70%),
      radial-gradient(ellipse 70px 40px at 46% 72%, var(--orange-light), transparent 70%),
      radial-gradient(ellipse 80px 44px at 66% 30%, var(--orange-light), transparent 70%),
      radial-gradient(ellipse 70px 40px at 84% 75%, var(--orange-light), transparent 70%),
      var(--orange);
  }
  .header-orange .band-title { margin-right: 22px; }

  .footer-lime { top: 656px; justify-content: flex-end; }
  .footer-lime .band-pattern {
    background:
      radial-gradient(ellipse 50px 18px at 10% 50%, var(--lime-light), transparent 70%),
      radial-gradient(ellipse 50px 18px at 30% 50%, var(--lime-light), transparent 70%),
      radial-gradient(ellipse 50px 18px at 50% 50%, var(--lime-light), transparent 70%),
      radial-gradient(ellipse 50px 18px at 70% 50%, var(--lime-light), transparent 70%),
      var(--lime);
  }
  .footer-lime .band-title { margin-right: 23px; }
</style>
</head>
<body>
  <section class="band header-band header-teal">
    <div class="band-pattern" role="img" aria-label="Teal pattern of white swirling spirals"></div>
    <h1 class="band-title">Sports Day</h1>
  </section>

  <section class="band footer-band footer-forest">
    <svg width="847" height="27" viewBox="0 0 847 27" role="img" aria-label="Green pattern of overlapping fish-scale shapes in two parts">
      <defs>
        <linearGradient id="scaleTone" x1="0" y1="0" x2="0" y2="1">
          <stop offset="0" stop-color="var(--forest)"/>
          <stop offset="0.5" stop-color="var(--forest-light)"/>
          <stop offset="1" stop-color="var(--forest-mid)"/>
        </linearGradient>
      </defs>
      <polygon points="0,0 324,0 313,27 0,27" fill="url(#scaleTone)"/>
      <polygon points="540,0 847,0 847,27 531,27" fill="url(#scaleTone)"/>
    </svg>
    <p class="band-title">Primary School Name 2014</p>
  </section>

  <section class="band header-band header-orange">
    <div class="band-pattern" role="img" aria-label="Orange pattern of white swirling spirals"></div>
    <h1 class="band-title">Sports Day</h1>
  </section>

  <section class="band footer-band footer-lime">
    <div class="band-pattern" role="img" aria-label="Lime green pattern of white swirling spirals"></div>
    <p class="band-title">Primary School Name 2014</p>
  </section>
</body>
</html>
```